Letterhead for Dane Holloway

I need a letterhead based on the business card design

Industry/Entity Type

Business

Requirements
Must have
• Footer: Dane Holloway Naturopath
Shop 3042c, 451 Marrow Lane, Sydney 2000

```html
<!DOCTYPE html>
<html lang="en">
<head>
<meta charset="utf-8">
<title>Dane Holloway Naturopath – Letterhead</title>
<link rel="stylesheet" href="https://fonts.googleapis.com/css2?family=Montserrat:wght@400;500&family=Nunito:wght@600&display=swap">
<style>
  :root {
    --backdrop: #3a3a3a;
    --paper: #ffffff;
    --brand-orange: #f28a24;
    --foliage-soft: rgba(248, 206, 160, 0);
    --foliage-mid: rgba(248, 206, 160, 0.75);
    --foliage-deep: #f6c594;
    --footer-text: #ffffff;
  }
  * { box-sizing: border-box; margin: 0; padding: 0; }
  html, body {
    width: 1200px;
    height: 1000px;
    overflow: hidden;
    background: var(--backdrop);
  }
  .canvas {
    position: relative;
    width: 1200px;
    height: 1000px;
  }
  .letterhead {
    position: absolute;
    left: 255px;
    top: 6px;
    width: 698px;
    height: 988px;
    background: var(--paper);
    overflow: hidden;
  }
  .brand {
    position: absolute;
    left: 149px;
    top: 66px;
    transform: translateX(-50%);
    text-align: center;
    font-family: "Montserrat", sans-serif;
    color: var(--brand-orange);
    white-space: nowrap;
  }
  .brand-name {
    display: block;
    font-weight: 500;
    font-size: 24px;
    line-height: 30px;
    letter-spacing: 0.3px;
  }
  .brand-rule {
    display: block;
    width: 148px;
    height: 2px;
    margin: 21px auto 0;
    background: var(--brand-orange);
  }
  .brand-practice {
    display: block;
    margin-top: 19px;
    font-weight: 400;
    font-size: 13px;
    line-height: 16px;
    letter-spacing: 2.6px;
    padding-left: 2.6px;
  }
  .foliage {
    position: absolute;
    left: 440px;
    top: 240px;
    width: 258px;
    height: 715px;
    background:
      radial-gradient(ellipse 120% 80% at 100% 75%, var(--foliage-deep) 0%, var(--foliage-mid) 45%, var(--foliage-soft) 100%);
  }
  .footer-band {
    position: absolute;
    left: 0;
    bottom: 0;
    width: 100%;
    height: 33px;
    background: var(--brand-orange);
    display: flex;
    align-items: center;
    justify-content: space-evenly;
    font-family: "Nunito", sans-serif;
    font-weight: 600;
    font-size: 10px;
    color: var(--footer-text);
  }
  .footer-divider { opacity: 0.9; }
</style>
</head>
<body>
<div class="canvas">
  <div class="letterhead">
    <div class="brand">
      <span class="brand-name">DANE HOLLOWAY</span>
      <span class="brand-rule"></span>
      <span class="brand-practice">NATUROPATHY</span>
    </div>

    <div class="foliage" role="img" aria-label="Cluster of large translucent peach leaves rising from the lower right corner"></div>

    <footer class="footer-band">
      <span>daneholloway.com.au</span>
      <span class="footer-divider">|</span>
      <span>Shop 3042c, 451 Marrow Lane, Sydney 2000</span>
      <span class="footer-divider">|</span>
      <span>dhnaturopath@mailbox.com</span>
      <span class="footer-divider">|</span>
      <span>0400 555 218</span>
    </footer>
  </div>
</div>
</body>
</html>
```